Label Design for Climbing Chalk (fitness category)

I am looking for someone to design a front and back label for a bottle of liquid chalk. Liquid chalk is used in gyms, gymnastics, climbing to prevent your hands from getting moist and increase friction. I'm uploading some design motivations that I like.

The bottle is going to be black and I want the label to be clear. You have free reign of how you want to approach this design. Below are more specifics for the sizing:

*Attached is a picture of a competitor product (Tor Hold Liquid Chalk). Please don't use this for motivation, their label is very bad. I'm attaching a picture so that you can see what the bottle looks like.
*Attached are design motivations that I like
*The bottle is 50 ml, it's 3.75 inches tall, 2 inches wide and 1.25 inches in depth.
*The label can be square or oval (it's up to you). The size of the label needs to be 1,25 x 2.25 inches.
*Name of the product: Varnel Liquid Chalk
*Label needs to have the following Required Text. You can arrange it however you like:
- (50 ml)
- Made by USA Competitive Athletes for Athletes. Increases grip and lasts 3-4 times longer than regular chalk.
- Directions: Shake well. Squeeze some Varnel Liquid Chalk into your hand and rub your hands together. Let your hands air dry for about 10 seconds. To remove the chalk wash your hands with light soap.
Warning: Avoid contact with Eyes. Do not use on broken skin. Do not ingest. Keep out of reach of small children.
- Ingredients: Magnesium carbonate, SD Alcohol, hydroxypropylcellulose, colophonium.

Target Market(s)

Fitness, Athletes, Rock Climbers, Weight Lifters, Gymnasts, etc

Industry/Entity Type

Fitness

Font styles to use
Sans Serif

Colors

Designer to choose colors to be used in the design.

Requirements
Must have
• Please see Project Description for required text. The bottle is going to be black and I want the clear label so please be creative with the colors that would look good
Nice to have
• Please see attached branding ideas that I liked for font and colors. You don't have to strictly stick to them, these are just some of the ones I liked. Be creative and put your best foot forward.

```html
<!DOCTYPE html>
<html lang="en">
<head>
<meta charset="utf-8">
<title>Varnel Liquid Chalk – Front and Back Labels</title>
<link href="https://fonts.googleapis.com/css2?family=Libre+Baskerville:wght@400;700&family=Josefin+Sans:wght@300;400;600&display=swap" rel="stylesheet">
<style>
  :root {
    --backdrop: #333333;
    --label-black: #0b0b0b;
    --label-glow: #4a4a4a;
    --gold: #b8913a;
    --ink-white: #f4f4f4;
    --ink-soft: #e2e2e2;
    --figure-tone: #d9d9d9;
  }
  html, body {
    margin: 0;
    padding: 0;
    width: 1200px;
    height: 1200px;
    overflow: hidden;
    background: var(--backdrop);
  }
  .canvas {
    position: relative;
    width: 1200px;
    height: 1200px;
  }
  .label {
    position: absolute;
    top: 230px;
    width: 340px;
    height: 720px;
    border-radius: 170px;
    background:
      radial-gradient(ellipse 60% 35% at 50% 52%, var(--label-glow) 0%, rgba(40,40,40,0.6) 45%, transparent 80%),
      var(--label-black);
    overflow: hidden;
    color: var(--ink-white);
  }
  .label--front { left: 170px; }
  .label--back { left: 690px; }

  .frame-outer, .frame-inner {
    position: absolute;
    border-style: solid;
    border-color: var(--gold);
    pointer-events: none;
  }
  .frame-outer { inset: 9px; border-width: 2px; border-radius: 161px; }
  .frame-inner { inset: 15px; border-width: 1.5px; border-radius: 155px; }

  .texture {
    position: absolute;
    left: 0; right: 0; bottom: 0;
    height: 330px;
    background: linear-gradient(165deg, transparent 0%, rgba(90,90,90,0.35) 35%, rgba(60,60,60,0.25) 60%, rgba(20,20,20,0.1) 100%);
  }

  .figure {
    position: absolute;
    left: 50%;
    transform: translateX(-50%);
    border-radius: 10px;
    background: linear-gradient(180deg, var(--figure-tone), #bdbdbd);
  }
  .label--front .figure { top: 58px; width: 150px; height: 180px; }
  .label--back .figure { top: 42px; width: 130px; height: 120px; }

  .brand {
    position: absolute;
    left: 0; right: 0;
    text-align: center;
    font-family: "Libre Baskerville", serif;
    font-weight: 700;
    letter-spacing: 1px;
    color: var(--ink-white);
  }
  .label--front .brand { top: 248px; font-size: 50px; }
  .label--back .brand { top: 168px; font-size: 44px; }

  .rule {
    position: absolute;
    left: 60px; right: 60px;
    height: 1.5px;
    background: var(--ink-soft);
  }

  .product-vertical {
    position: absolute;
    top: 334px;
    left: 0; right: 0;
    height: 180px;
    display: flex;
    justify-content: center;
    align-items: flex-start;
    gap: 6px;
    font-family: "Libre Baskerville", serif;
    font-size: 38px;
    letter-spacing: 0;
    color: var(--ink-soft);
  }
  .product-vertical span {
    writing-mode: vertical-rl;
    transform: rotate(180deg);
    line-height: 1;
  }

  .tagline {
    position: absolute;
    top: 528px;
    left: 0; right: 0;
    text-align: center;
    font-family: "Libre Baskerville", serif;
    font-size: 14.5px;
  }
  .claim {
    position: absolute;
    top: 566px;
    left: 40px; right: 26px;
    font-family: "Libre Baskerville", serif;
    font-size: 13.5px;
    letter-spacing: -0.4px;
    line-height: 20px;
    padding-left: 18px;
    text-indent: -14px;
  }
  .volume {
    position: absolute;
    top: 640px;
    left: 0; right: 0;
    text-align: center;
    font-family: "Libre Baskerville", serif;
    font-size: 19px;
  }

  .product-sub {
    position: absolute;
    top: 222px;
    left: 0; right: 0;
    text-align: center;
    font-family: "Libre Baskerville", serif;
    font-size: 22px;
    color: var(--ink-soft);
  }
  .copy {
    position: absolute;
    top: 264px;
    left: 42px; right: 40px;
    font-family: "Josefin Sans", sans-serif;
    font-weight: 400;
    font-size: 16px;
    letter-spacing: 0.3px;
    line-height: 22.5px;
    color: var(--ink-white);
  }
  .copy p { margin: 0; }
  .copy strong { font-weight: 600; }
  .origin {
    position: absolute;
    top: 618px;
    left: 0; right: 0;
    text-align: center;
    font-family: "Josefin Sans", sans-serif;
    font-size: 22px;
    letter-spacing: 0.5px;
  }
</style>
</head>
<body>
<main class="canvas">

  <section class="label label--front" aria-label="Front label">
    <div class="texture" role="img" aria-label="Halftone dot texture sweeping across the lower label"></div>
    <div class="frame-outer"></div>
    <div class="frame-inner"></div>
    <div class="figure" role="img" aria-label="White silhouette of an athlete holding a barbell overhead"></div>
    <div class="brand">VARNEL</div>
    <div class="rule" style="top:320px;"></div>
    <div class="product-vertical"><span>LIQUID</span><span>CHALK</span></div>
    <div class="tagline">Competitive Athletes for Athletes</div>
    <div class="rule" style="top:553px;"></div>
    <div class="claim">★ Increases grip and lasts 3-4 times longer than regular chalk</div>
    <div class="volume">50 ml</div>
  </section>

  <section class="label label--back" aria-label="Back label">
    <div class="texture" role="img" aria-label="Halftone dot texture sweeping across the lower label"></div>
    <div class="frame-outer"></div>
    <div class="frame-inner"></div>
    <div class="figure" role="img" aria-label="White silhouette of an athlete holding a barbell overhead"></div>
    <div class="brand">VARNEL</div>
    <div class="product-sub">LIQUID CHALK</div>
    <div class="copy">
      <p>Directions: Shake well. Squeeze some Varnel Liquid Chalk into your hand and rub your hands together. Let your hands air dry for about 10 seconds. To remove the chalk wash your hands with light soap.</p>
      <p><strong>Warning:</strong> Avoid contact with Eyes. Do not use on broken skin. Do not ingest. Keep out of reach of small children.</p>
      <p><strong>Ingredients:</strong> Magnesium carbonate, SD Alcohol, hydroxypropylcellulose, colophonium.</p>
    </div>
    <div class="origin">Made by USA</div>
  </section>

</main>
</body>
</html>
```